Marketing Brochure - Conjunction event

We need a brochure for clients/conjunction real estate agents to view the type of projects NESTA452 have available.
As a guideline of our requirements, please refer to our company profile. As you can see it is a simple elegant professional image we are after.
We are a Real Estate company specialise in off the plans project marketing. We have sale teams to sell the projects/ residential properties but also conjunction with other real estate agents. This is the first time we decided to use CraftHive to design our brochure. If pleasing results, ongoing we will have many more design projects to do.

Target Market(s)

Clients / real estate agents

Industry/Entity Type

Real Estate

Font styles to use
Sans Serif

Colors
ffffff
ef484e

Requirements
Must have
• All the details in the documents, Encourage creative designs.
• Company logo and the black banner as seen on company profile brochure
Nice to have
• similar to our company profile brochure( file attached)
Should not have
• Funky or too loud type image

```html
<!DOCTYPE html>
<html lang="en">
<head>
<meta charset="utf-8">
<title>Why NESTA452 – Brochure Page 4</title>
<link rel="stylesheet" href="https://fonts.googleapis.com/css2?family=Anton&family=Arimo:wght@400;700&display=swap">
<style>
  :root {
    --brand-red: #ef484e;
    --deep-red: #d8323b;
    --ring-red: #e4515a;
    --soft-pink: #f27a80;
    --pale-pink: #f7b3b6;
    --banner-yellow: #f9a51e;
    --white: #ffffff;
    --photo-sky: #a9c4e2;
    --photo-blue: #4a6fae;
    --photo-dusk: #27335a;
    --photo-night: #1c2434;
    --photo-warm: #e0a25c;
    --photo-leaf: #3f4a2e;
  }
  * { margin: 0; padding: 0; box-sizing: border-box; }
  html, body { width: 928px; height: 1200px; overflow: hidden; background: var(--white); }
  .page { position: relative; width: 928px; height: 1200px; font-family: "Arimo", Arial, sans-serif; }
  .page-art { position: absolute; inset: 0; }
  .title-banner {
    position: absolute; left: 14px; top: 37px; width: 325px; height: 63px;
    background: var(--banner-yellow);
    clip-path: polygon(0 0, 100% 0, 85% 100%, 0 100%);
    display: flex; align-items: center; padding-left: 21px;
  }
  .title-banner h1 {
    font-family: "Anton", Impact, sans-serif; font-weight: 400;
    color: var(--white); font-size: 30px; letter-spacing: 0.3px;
  }
  .intro { position: absolute; left: 47px; top: 731px; width: 850px; color: var(--white); }
  .intro h2 { font-size: 19px; font-weight: 700; line-height: 24px; margin-bottom: 14px; }
  .intro-columns { display: flex; }
  .intro-column { white-space: nowrap; }
  .intro-column--left { width: 435px; }
  .intro p { font-size: 18.3px; line-height: 23.2px; letter-spacing: 0.15px; }
  .intro p + p { margin-top: 23.2px; }
  .page-number {
    position: absolute; left: 830px; top: 1102px; width: 40px; height: 40px;
    display: flex; align-items: center; justify-content: center;
    font-family: "Anton", Impact, sans-serif; font-size: 23px; color: var(--deep-red);
  }
</style>
</head>
<body>
<main class="page">
  <svg class="page-art" width="928" height="1200" viewBox="0 0 928 1200">
    <defs>
      <linearGradient id="photoBase" x1="0" y1="0" x2="0.35" y2="1">
        <stop offset="0" stop-color="var(--photo-sky)"/>
        <stop offset="0.3" stop-color="var(--photo-blue)"/>
        <stop offset="0.62" stop-color="var(--photo-dusk)"/>
        <stop offset="1" stop-color="var(--photo-night)"/>
      </linearGradient>
      <radialGradient id="photoGlow" cx="0.45" cy="0.88" r="0.55">
        <stop offset="0" stop-color="var(--photo-warm)" stop-opacity="0.95"/>
        <stop offset="0.6" stop-color="var(--photo-warm)" stop-opacity="0.35"/>
        <stop offset="1" stop-color="var(--photo-warm)" stop-opacity="0"/>
      </radialGradient>
      <radialGradient id="photoShade" cx="0.9" cy="0.55" r="0.4">
        <stop offset="0" stop-color="var(--photo-leaf)" stop-opacity="0.85"/>
        <stop offset="1" stop-color="var(--photo-leaf)" stop-opacity="0"/>
      </radialGradient>
      <clipPath id="panelClip"><rect x="14" y="700" width="897" height="482" rx="14"/></clipPath>
    </defs>
    <rect class="corner-block" x="14" y="14" width="110" height="214" rx="12" fill="var(--brand-red)"/>
    <rect class="corner-block" x="730" y="14" width="181" height="170" rx="12" fill="var(--brand-red)"/>
    <g class="feature-photo" role="img" aria-label="Evening render of a modern apartment tower with a ground-floor café, street trees and a parked car">
      <polygon points="118,15 735,15 742,185 800,160 880,150 920,120 920,667 7,667 7,245 118,232" fill="url(#photoBase)"/>
      <polygon points="118,15 735,15 742,185 800,160 880,150 920,120 920,667 7,667 7,245 118,232" fill="url(#photoShade)"/>
      <polygon points="118,15 735,15 742,185 800,160 880,150 920,120 920,667 7,667 7,245 118,232" fill="url(#photoGlow)"/>
    </g>
    <polygon class="panel-pointer" points="92,700 103,681 116,700" fill="var(--brand-red)"/>
    <rect class="info-panel" x="14" y="700" width="897" height="482" rx="14" fill="var(--brand-red)"/>
    <g clip-path="url(#panelClip)">
      <rect class="footer-stripe" x="14" y="1150" width="897" height="8" fill="var(--soft-pink)"/>
      <rect class="footer-base" x="14" y="1158" width="897" height="30" fill="var(--deep-red)"/>
      <circle cx="850" cy="1122" r="60" fill="var(--deep-red)"/>
      <circle cx="850" cy="1122" r="47" fill="var(--ring-red)"/>
      <circle cx="850" cy="1122" r="34" fill="var(--soft-pink)"/>
      <circle cx="850" cy="1122" r="23" fill="var(--pale-pink)"/>
      <circle cx="850" cy="1122" r="18" fill="var(--white)"/>
    </g>
    <circle class="target-dot" cx="778" cy="1112" r="24" fill="var(--banner-yellow)"/>
    <circle cx="778" cy="1112" r="17" fill="var(--soft-pink)"/>
    <circle cx="778" cy="1112" r="10" fill="var(--banner-yellow)"/>
    <circle cx="778" cy="1112" r="5" fill="var(--pale-pink)"/>
  </svg>

  <div class="title-banner"><h1>WHY NESTA452 ?</h1></div>

  <section class="intro">
    <h2>Our Modus Operandi is Simple</h2>
    <div class="intro-columns">
      <div class="intro-column intro-column--left">
        <p>Welcome to NESTA452. We are an Australia<br>established and based Real Estate Agency<br>with our head office located in Harlow Vale.<br>Our company offers a comprehensive range<br>of property services to our clients locally<br>and overseas mainly along the Pacific region.<br>These services include the standard real<br>estate businesses such as local properties<br>buy/sell and property management.</p>
        <p>These services include the standard real<br>estate businesses such as local properties<br>buy/sell and property management.</p>
      </div>
      <div class="intro-column">
        <p>Our company offers a comprehensive range<br>of property services to our clients locally<br>and overseas mainly along the Pacific region.<br>These services include the standard real<br>estate businesses such as local properties<br>buy/sell and property management. Welcome<br>to NESTA452. We are an Australia<br>established and based Real Estate Agency<br>with our head office located in Harlow Vale.</p>
      </div>
    </div>
  </section>

  <div class="page-number">4</div>
</main>
</body>
</html>
```